Tide of the Modest : Thriving amid network change by Curtis Oyelaran

Need a book cover, front, back and 3D. We would like the cover to have a digital globe that also shows blockchain/nodes. Best if it can also illustrate the idea of Tide of the modest. Please see the pictures which I have short-listed which can be potentially used for the book cover.

The book cover should look like an expert book and I have attached some graphics that we can potentially buy and use for this book cover.

The text for the back cover is attached in the docx. Some text is not finished, please leave empty spaces for this.

Target Market(s)

Those interested in technology, blockchain, business, finance and law. The more informed readers.

Industry/Entity Type

Digital

Font styles to use
Sans Serif

Colors
31a5d6
0555a3
33a6d7
3176b5
85cae6
85acd3
cee9f5
cedeed

Requirements
Must have
• We would like you to consider the images attached here for the book design. We want it to be simple, clear and like an expert book. Please refer to the docx for the back cover text. Leave some text spaces for text not yet written.
• We require, front cover, back cover and 3D. You can do the 3D after your design is selected.
Nice to have
• The cover should be classy and timeless. It should have the blockchain / nodes. Will be great if the book cover can convey the meaning of Tide of the Modest, through the text. eg. one of the images, look like a "Lanternfall" type photo, maybe the text can be somewhat Lanternfall like.
• You are welcome to suggest photos not attached here.
• Once we have identified the winner, we will proceed to purchase the photo for our use.
• Text can be Lato, but not necessary.
Should not have
• Too messy or too many ideas. Just a simple clear idea.

```html
<!DOCTYPE html>
<html lang="en">
<head>
<meta charset="utf-8">
<title>Tide of the Modest — Cover Spread</title>
<link rel="stylesheet" href="https://fonts.googleapis.com/css2?family=Anton&family=Lato:wght@300;400;700;900&display=swap">
<style>
  :root {
    --night: #030b1c;
    --navy: #07193a;
    --deep-blue: #0555a3;
    --mid-blue: #3176b5;
    --sky: #31a5d6;
    --sky-soft: #85cae6;
    --ice: #cee9f5;
    --white: #ffffff;
    --spine-author: #2a67d6;
  }
  * { margin: 0; padding: 0; box-sizing: border-box; }
  html, body { width: 1200px; height: 867px; overflow: hidden; background: var(--night); }
  .spread {
    position: relative; width: 1200px; height: 867px; overflow: hidden;
    background:
      radial-gradient(ellipse at 80% 20%, #0b2350 0%, transparent 55%),
      linear-gradient(180deg, var(--navy) 0%, var(--night) 100%);
    font-family: "Lato", sans-serif; color: var(--white);
  }
  .display { font-family: "Anton", sans-serif; text-transform: uppercase; font-weight: 400; line-height: 0.92; }

  /* back cover */
  .back-title { position: absolute; left: 77px; top: 48px; }
  .back-title .line-1 { display: block; font-size: 36px; }
  .back-title .line-2 { display: block; font-size: 56px; margin-top: 3px; }
  .back-lead { position: absolute; left: 253px; top: 44px; width: 232px; font-size: 16px; font-weight: 700; line-height: 1.5; }
  .back-body { position: absolute; left: 77px; top: 164px; width: 405px; font-size: 12.6px; line-height: 15.2px; text-align: justify; }
  .back-body p + p { margin-top: 18px; }
  .takeaways { position: absolute; left: 168px; top: 628px; width: 300px; font-size: 12.6px; line-height: 1.4; }
  .takeaways h3 { font-size: 15px; font-weight: 700; margin-bottom: 12px; }
  .takeaways ol { list-style: none; }
  .takeaways li { margin-bottom: 10px; }
  .takeaways .num { color: var(--sky); font-weight: 700; font-size: 15px; }
  .site { position: absolute; left: 77px; top: 805px; font-size: 15px; font-weight: 700; }

  /* spine */
  .spine-title, .spine-author {
    position: absolute; writing-mode: vertical-rl; white-space: nowrap; line-height: 1;
  }
  .spine-title { left: 569px; top: 50px; font-size: 56px; }
  .spine-author { left: 575px; top: 526px; font-size: 42px; color: var(--spine-author); }

  /* front cover */
  .globe {
    position: absolute; left: 600px; top: 400px; width: 600px; height: 467px;
    background:
      radial-gradient(circle at 73% 22%, #ffffff 0%, #bfe8ff 4%, #3fb1ea 13%, rgba(5,85,163,0.55) 32%, transparent 56%),
      radial-gradient(ellipse 100% 115% at 62% 118%, #1a86d0 0%, #0a4c8f 40%, #052552 66%, transparent 80%);
  }
  .front-title { position: absolute; left: 631px; width: 569px; text-align: center; top: 106px; }
  .front-title .line-1 { display: block; font-size: 77px; }
  .front-title .line-2 { display: block; font-size: 115px; margin-top: 13px; }
  .subtitle { position: absolute; left: 631px; width: 569px; top: 336px; text-align: center; font-size: 23px; font-weight: 400; color: var(--ice); }
  .front-author { position: absolute; left: 631px; width: 569px; top: 768px; text-align: center; font-size: 56px; }
</style>
</head>
<body>
<main class="spread">
  <section class="back-cover">
    <h2 class="back-title display"><span class="line-1">Tide of the</span><span class="line-2">Modest</span></h2>
    <p class="back-lead">Most people would have heard of Veltcoin and the underlying technology known as Blockchain. There have been two sides of the</p>
    <div class="back-body">
      <p>Most people would have heard of Veltcoin and the underlying technology known as Blockchain. There have been two sides of the arguments.</p>
      <p>On the side of the bankers and the regulators, their criticism of Veltcoin is that Veltcoin is unregulated and not backed by any asset. On the side of the Blockchain community, the regularly heard argument is that Veltcoin or CryptoAssets are limited and rare thus giving value to Veltcoin or CryptoAssets.</p>
      <p>Both of these arguments are incomplete and do not explain the Blockchain evolution. The bankers and regulators are incomplete with their well intended advice because regulating an emerging historical trend caps the potential it can create in a society and that the backing of the dollar or other assets are still conditioned on various macroeconomic trend. The price of a real estate or even gold is still decided by market forces. Veltcoin or cryptoassets cannot be valuable just by virtue of its limitedness - there are a lot of things that are limited that may not be valuable.</p>
      <p>Cryptoassets are valuable by virtue of how it overcomes the transactional friction that has been inherent in human history. Overcoming the transactional friction is the looking at the blockchain evolution via the eyes of an economist - that it would catalyse trading and create immense value for participating parties and create social utility for the world at large, and we are just at the beginning of the Blockchain Evolution.</p>
    </div>
    <div class="takeaways">
      <h3>Key take any</h3>
      <ol>
        <li><span class="num">1.</span> Most people would have heard of Veltcoin and the underlying technology known.</li>
        <li><span class="num">2.</span> Most people would have heard of Veltcoin and the underlying technology known.</li>
        <li><span class="num">3.</span> Most people would have and the underlying technology.</li>
      </ol>
    </div>
    <p class="site">www.tideofthemodest.com.sg</p>
  </section>

  <section class="spine">
    <h2 class="spine-title display">Tide of the Modest</h2>
    <p class="spine-author display">Curtis Oyelaran</p>
  </section>

  <section class="front-cover">
    <div class="globe" role="img" aria-label="Digital globe seen from space with glowing blockchain node network and sunrise glare"></div>
    <h1 class="front-title display"><span class="line-1">Tide of the</span><span class="line-2">Modest</span></h1>
    <p class="subtitle">Thriving amid network change</p>
    <p class="front-author display">Curtis Oyelaran</p>
  </section>
</main>
</body>
</html>
```